Quiet Harbor

The subtitle is "Seven Lamps for the Wandering Heart."

Target Market(s)

Religious people

Industry/Entity Type

Religious

Font styles to use
Serif
Script

Requirements
Must have
• I'd like something with a "medical" feel
Should not have
• Pictures of people

```html
<!DOCTYPE html>
<html lang="en">
<head>
<meta charset="utf-8">
<title>Quiet Harbor — Seven Lamps for the Wandering Heart</title>
<link rel="stylesheet" href="https://fonts.googleapis.com/css2?family=Dancing+Script:wght@700&family=Playfair+Display:wght@700;900&display=swap">
<style>
  :root {
    --page-bg: #e8e9ea;
    --cover-teal: #83a0a2;
    --cover-teal-deep: #6f8d90;
    --gantry-light: #dfe6e8;
    --gantry-mid: #b9c6ca;
    --bore-light: #d3dcdd;
    --bore-mid: #bcc8cb;
    --bore-ring: #4f5c64;
    --title-ink: #2a3441;
    --outline-white: #ffffff;
    --subtitle-ink: #0b0b0b;
  }
  * { box-sizing: border-box; margin: 0; padding: 0; }
  html, body {
    width: 1200px; height: 864px; overflow: hidden;
    background: var(--page-bg);
  }
  .cover {
    position: absolute;
    left: 312px; top: 32px;
    width: 576px; height: 800px;
    overflow: hidden;
    background: linear-gradient(180deg, var(--cover-teal) 0%, var(--cover-teal) 40%, var(--cover-teal-deep) 100%);
    box-shadow: 0 10px 30px rgba(0,0,0,0.18);
  }
  .cover__gantry {
    position: absolute;
    left: 40px; top: 270px;
    width: 760px; height: 760px;
    border-radius: 50%;
    background: radial-gradient(circle at 50% 50%, var(--gantry-light) 0%, var(--gantry-mid) 55%, rgba(131,160,162,0) 72%);
  }
  .cover__scan-bore {
    position: absolute;
    left: 140px; top: 360px;
    width: 580px; height: 580px;
    border-radius: 50%;
    background: radial-gradient(circle at 42% 40%, var(--bore-light) 0%, #c8d2d4 55%, var(--bore-mid) 100%);
  }
  .cover__bore-ring {
    position: absolute;
    left: 134px; top: 354px;
    width: 592px; height: 592px;
  }
  .cover__brand {
    position: absolute;
    left: 40px; top: 28px;
    font-family: "Playfair Display", Georgia, serif;
    font-weight: 700;
    font-size: 20px;
    letter-spacing: 4px;
    text-transform: uppercase;
    color: var(--title-ink);
  }
  .cover__title {
    position: absolute;
    left: 34px; top: 62px;
    font-family: "Dancing Script", "Brush Script MT", cursive;
    font-weight: 700;
    font-size: 96px;
    line-height: 0.98;
    color: var(--title-ink);
    -webkit-text-stroke: 7px var(--outline-white);
    paint-order: stroke fill;
  }
  .cover__title-line { display: block; }
  .cover__title-line--indent { padding-left: 110px; }
  .cover__subtitle {
    position: absolute;
    right: 26px; bottom: 64px;
    font-family: "Playfair Display", Georgia, serif;
    font-weight: 900;
    font-size: 40px;
    letter-spacing: 0.5px;
    color: var(--subtitle-ink);
    -webkit-text-stroke: 8px var(--outline-white);
    paint-order: stroke fill;
  }
</style>
</head>
<body>
  <main class="cover">
    <div class="cover__gantry"></div>
    <div class="cover__scan-bore" role="img" aria-label="Photo of a medical CT scanner bore with a patient table and red laser guide lines"></div>
    <svg class="cover__bore-ring" viewBox="0 0 592 592" aria-hidden="true">
      <circle cx="296" cy="296" r="292" fill="none" stroke="var(--bore-ring)" stroke-width="4"/>
      <circle cx="296" cy="296" r="285" fill="none" stroke="#9aa8ad" stroke-width="2"/>
    </svg>
    <p class="cover__brand">Quiet Harbor</p>
    <h1 class="cover__title">
      <span class="cover__title-line">Seven Lamps</span>
      <span class="cover__title-line cover__title-line--indent">for the</span>
    </h1>
    <p class="cover__subtitle">WANDERING HEART</p>
  </main>
</body>
</html>
```